Relaunch kelvorin.com

I need someone to review my existing site at WordPress, make it more contemporary and visually appealing while preserving the content, which is quite text-dense, and improve the navigation. For example, if you go to https://kelvorin.com/claims-handled/ you will see links to dedicated pages for various client groups - I would like those to somehow be evident from the home page.

It would be simpler to keep it at WordPress but I am open to using a different CMS if necessary.

Fluency in Spanish would be useful, since part of the site is in Spanish.

Target Market(s)

Shipowners, vessel operators, ship managers

Industry/Entity Type

Marine insurance / marine transportation

Number of Pages Required

5+ page

Colors

Designer to choose colors to be used in the design.

Requirements
Must have
• Substantially preserve exciting content, but make it more accessible.
Nice to have
• This is an online brochure - we don't sell anything on line. I would like the theme to tie in to the colors in the existing logo, which we will keep.

```html
<!DOCTYPE html>
<html lang="en">
<head>
<meta charset="utf-8">
<title>The Kelvorin Company – Average Adjusters</title>
<link href="https://fonts.googleapis.com/css2?family=Poppins:wght@400;500;600&family=Libre+Baskerville:wght@400;700&display=swap" rel="stylesheet">
<style>
:root{
  --navy:#163f66;
  --navy-card:#1d4e7d;
  --red:#b8322a;
  --red-card:#c4453a;
  --ink:#222;
  --muted:#333;
  --topbar:#f2f4f8;
  --gray-band:#f5f5f5;
  --card-bg:#f3f6fb;
  --footer:#1e1e1e;
  --white:#fff;
}
*{box-sizing:border-box;margin:0;padding:0}
html,body{width:1200px;height:3330px;overflow:hidden}
body{font-family:"Poppins",sans-serif;color:var(--ink);background:var(--white);position:relative}
.serif{font-family:"Libre Baskerville",serif}
a{color:inherit;text-decoration:none}

/* top bar */
.topbar{height:46px;background:var(--topbar);position:relative;font-size:14px}
.topbar .contact{position:absolute;left:111px;top:13px;display:flex;gap:18px;align-items:center}
.topbar .contact span.ic{color:var(--red);margin-right:6px}
.socials{position:absolute;left:939px;top:0;display:flex}
.socials .s{width:38px;height:46px;border-left:1px solid #d9dde4;display:flex;align-items:center;justify-content:center}
.socials .s:last-child{border-right:1px solid #d9dde4}
.socials .s.active{background:var(--navy)}
.socials .s i{width:10px;height:10px;border-radius:50%;background:#222}
.socials .s.active i{background:#fff}

/* header */
.header{height:99px;position:relative;border-bottom:1px solid #eee}
.brand{position:absolute;left:111px;top:28px;display:flex;align-items:center;gap:10px;color:var(--red);font-weight:600;font-size:30px;letter-spacing:2px}
.brand .dot{width:14px;height:14px;background:var(--navy);border-radius:50%}
.nav{position:absolute;left:385px;top:40px;display:flex;gap:28px;font-size:15px;font-weight:500}
.nav a.current{color:var(--navy);border-bottom:2px solid var(--navy);padding-bottom:2px}
.btn{display:inline-flex;align-items:center;justify-content:center;background:var(--red);color:#fff;font-weight:600;border-radius:30px;font-size:15px;text-transform:uppercase}
.header .btn{position:absolute;left:930px;top:26px;width:159px;height:48px}

/* hero */
.hero{position:relative;height:650px;overflow:hidden;background:linear-gradient(180deg,#3b2c33 0%,#b86a3a 30%,#e89a3c 45%,#7a4a3a 65%,#2e2a35 100%)}
.hero .photo{position:absolute;inset:0}
.hero .bar{position:absolute;left:111px;top:107px;width:4px;height:314px;background:#fff}
.hero h1{position:absolute;left:145px;top:110px;color:#fff;font-size:40px;line-height:50px;font-weight:400}
.hero p{position:absolute;left:145px;top:273px;color:#fff;font-size:21px;line-height:31px}
.hero .btn{position:absolute;left:146px;top:359px;width:150px;height:46px}
.dots{position:absolute;left:1140px;top:254px;display:flex;flex-direction:column;gap:10px}
.dots i{width:12px;height:12px;border-radius:50%;background:rgba(255,255,255,.5)}
.dots i.on{background:#fff}
.hero svg.wave{position:absolute;left:0;bottom:0}

/* about */
.about{position:relative;height:572px}
.about .ring{position:absolute;left:111px;top:7px;width:446px;height:446px}
.about h2{position:absolute;left:612px;top:26px;font-size:44px;color:var(--navy);font-weight:400}
.rule{display:block;width:84px;height:4px;background:var(--red)}
.about .rule{position:absolute;left:612px;top:79px}
.about .text{position:absolute;left:612px;top:100px;width:480px;font-size:16.5px;line-height:27.5px;color:var(--muted)}
.about .text p+p{margin-top:14px}
.about .btn{position:absolute;left:612px;top:405px;width:152px;height:47px}

/* claims */
.claims{position:relative;height:818px;background:var(--gray-band);text-align:center}
.claims h2{padding-top:78px;font-size:46px;color:var(--navy);font-weight:400}
.claims .rule{margin:6px auto 0}
.claims .lead{width:960px;margin:34px auto 0;font-size:16px;line-height:26.5px;color:var(--muted)}
.claims h3{margin-top:20px;font-size:19px;font-weight:500;color:#222}
.cards{position:absolute;left:0;top:398px;display:flex}
.card{width:300px;height:420px;background:var(--navy-card);color:#fff;border-radius:20px;padding:34px 28px 0;text-align:center}
.card.hl{background:linear-gradient(160deg,#b93b31,#d25448)}
.card .icon{width:88px;height:88px;border-radius:50%;background:var(--red);margin:0 auto;display:flex;align-items:center;justify-content:center}
.card.hl .icon{background:#fff}
.card h4{margin-top:26px;font-size:18px;font-weight:600}
.card .pip{width:9px;height:9px;border-radius:50%;background:rgba(255,255,255,.4);margin:10px auto 0}
.card p{margin-top:12px;font-size:14.5px;line-height:25px;height:125px}
.card .more{display:inline-flex;align-items:center;justify-content:center;width:151px;height:47px;border-radius:30px;background:#fff;color:var(--red);font-weight:500;font-size:15px;margin-top:14px}
.card.hl .more{background:var(--navy);color:#fff}

/* resources */
.resources{position:relative;height:750px;text-align:center}
.resources h2{padding-top:104px;font-size:42px;color:var(--navy);font-weight:400}
.resources .rule{margin:4px auto 0;width:120px}
.res-grid{position:absolute;left:111px;top:280px;display:flex;gap:33px}
.res{width:304px;height:369px;background:var(--card-bg);border-radius:16px;overflow:hidden}
.res.hl{background:#fff;box-shadow:0 6px 18px rgba(0,0,0,.15);border-bottom:5px solid var(--red)}
.res .img{height:222px}
.res h5{padding-top:22px;font-size:19.5px;font-weight:500;line-height:31px;color:#222}
.resources .btn{position:absolute;left:524px;top:2814px;}
.view{position:absolute;left:524px;top:645px;width:152px;height:48px}

/* footer */
.footer{position:absolute;left:0;top:2935px;width:1200px;height:395px;background:var(--footer);color:#fff}
.footer .brand{left:111px;top:72px;color:#fff;font-size:32px}
.footer .brand .dot{background:#fff}
.footer .about-f{position:absolute;left:111px;top:158px;width:470px;font-size:15px;line-height:27.5px}
.footer .about-f a{text-decoration:underline;margin-left:6px}
.footer h6{position:absolute;top:80px;font-size:17px;font-weight:500}
.links{position:absolute;left:597px;top:124px;list-style:none;font-size:15px;line-height:31px}
.links li::before{content:"•";color:var(--red);margin-right:22px}
.cinfo{position:absolute;left:794px;top:124px;font-size:15px;line-height:25px}
.cinfo div{display:flex;gap:14px;margin-bottom:12px}
.cinfo .ic{color:var(--red);width:14px}
.footer .divider{position:absolute;left:111px;top:330px;width:978px;height:1px;background:#444}
.copy{position:absolute;left:397px;top:350px;font-size:13px}
.fsoc{position:absolute;left:930px;top:343px;display:flex;gap:10px}
.fsoc i{width:32px;height:32px;border-radius:50%;background:#fff}
.fsoc i.on{background:var(--red)}
.totop{position:absolute;left:1118px;top:303px;width:46px;height:46px;border-radius:50%;background:var(--navy-card);display:flex;align-items:center;justify-content:center}
</style>
</head>
<body>

<div class="topbar">
  <div class="contact">
    <span><span class="ic">&#9990;</span>+1 (555) 014-2290</span>
    <span>|</span>
    <span><span class="ic">&#9993;</span>info@kelvorin.com</span>
  </div>
  <div class="socials">
    <a class="s active" aria-label="Social profile 1"><i></i></a>
    <a class="s" aria-label="Social profile 2"><i></i></a>
    <a class="s" aria-label="Social profile 3"><i></i></a>
    <a class="s" aria-label="Social profile 4"><i></i></a>
  </div>
</div>

<header class="header">
  <a class="brand"><span class="dot"></span>KELVORIN</a>
  <nav class="nav">
    <a class="current">Home</a><a>Claims Handled</a><a>General Average</a><a>Staff</a><a>Resources</a>
  </nav>
  <a class="btn">Contact Us</a>
</header>

<section class="hero">
  <div class="photo" role="img" aria-label="Container ship sailing at sunset over the sea"></div>
  <span class="bar"></span>
  <h1 class="serif">WELCOME TO<br>THE KELVORIN<br>COMPANY</h1>
  <p>Average adjusters and marine<br>insurance consultants</p>
  <a class="btn">Get Started</a>
  <div class="dots"><i></i><i class="on"></i><i></i><i></i></div>
  <svg class="wave" width="1200" height="170" viewBox="0 0 1200 170">
    <path d="M0 170 C250 20 500 5 700 40 C900 75 1100 110 1200 135 L1200 170 Z" fill="var(--navy)"/>
    <path d="M0 170 C250 40 500 30 700 62 C900 95 1100 125 1200 150 L1200 170 Z" fill="#fff"/>
  </svg>
</section>

<section class="about">
  <svg class="ring" viewBox="0 0 446 446">
    <circle cx="223" cy="223" r="223" fill="var(--red)"/>
    <circle cx="238" cy="238" r="207" fill="#fff"/>
    <defs><linearGradient id="shipfill" x1="0" y1="0" x2="0" y2="1"><stop offset="0" stop-color="#cfe2f2"/><stop offset=".55" stop-color="#8fb0cc"/><stop offset="1" stop-color="#4c7fa6"/></linearGradient></defs>
    <circle cx="238" cy="238" r="205" fill="url(#shipfill)" role="img" aria-label="Container ship under a protective shield emblem"/>
  </svg>
  <h2 class="serif">ABOUT US</h2>
  <span class="rule"></span>
  <div class="text">
    <p>The Kelvorin Company is a leading, independent average adjuster, in operation since 1998. We take pride in the speed of our response, the accuracy of our work, the reasonableness of our fees and the professional standards we uphold.</p>
    <p>“Average” is believed to derive from an old Arabic word, “awar”, meaning “damage”. For centuries, average was a mechanism for dividing the risk inherent to a maritime adventure, with each merchant sharing in proportion to the profit, in the case of success</p>
  </div>
  <a class="btn">Learn More</a>
</section>

<section class="claims">
  <h2 class="serif">CLAIMS HANDLED</h2>
  <span class="rule"></span>
  <p class="lead">Here we briefly summarize the types of claim we principally handle. If you don’t see what you are looking for, tell us and we can discuss whether we can conscientiously take it on. Successful claim outcomes revolve around a combination of factors, including thinking clearly, writing clearly, communicating clearly with assureds about underwriters’ expectations and ensuring that surveyors produce coherent and comprehensive reports. These are all elements of the claim process that become second nature during a successful career.</p>
  <h3>For industry-segment focused descriptions, please visit our dedicated pages</h3>
  <div class="cards">
    <div class="card">
      <div class="icon"><svg width="40" height="40" viewBox="0 0 40 40" fill="#fff"><circle cx="13" cy="12" r="6"/><circle cx="27" cy="12" r="6"/><rect x="4" y="22" width="32" height="12" rx="6"/></svg></div>
      <h4>OWNERS</h4><div class="pip"></div>
      <p>All average adjusters are not created equal. Of particular relevance in the US, if your insurance brokers have average adjusters on staff</p>
      <a class="more">LEARN MORE</a>
    </div>
    <div class="card">
      <div class="icon"><svg width="40" height="40" viewBox="0 0 40 40" fill="#fff"><path d="M20 3 L34 8 V19 C34 28 27 34 20 37 C13 34 6 28 6 19 V8 Z"/></svg></div>
      <h4>INSURANCE BROKERS</h4><div class="pip"></div>
      <p>The Kelvorin Company is ideally suited to assisting independent brokers in developing new business and servicing and retaining existing business.</p>
      <a class="more">LEARN MORE</a>
    </div>
    <div class="card hl">
      <div class="icon"><svg width="36" height="40" viewBox="0 0 36 40" fill="var(--navy)"><path d="M4 2 H24 L32 10 V38 H4 Z"/><rect x="9" y="14" width="16" height="2.5" fill="#fff"/><rect x="9" y="20" width="16" height="2.5" fill="#fff"/><rect x="9" y="26" width="10" height="2.5" fill="#fff"/></svg></div>
      <h4>UNDERWRITERS</h4><div class="pip"></div>
      <p>Specialist opinions: How often have you turned to an attorney for an opinion on coverage and quantum only to find that your Insured interprets</p>
      <a class="more">LEARN MORE</a>
    </div>
    <div class="card">
      <div class="icon"><svg width="40" height="40" viewBox="0 0 40 40" fill="#fff"><circle cx="14" cy="11" r="7"/><path d="M2 34 C2 24 8 20 14 20 C18 20 20 21 22 23 V34 Z"/><rect x="22" y="22" width="16" height="13" rx="2"/></svg></div>
      <h4>ATTORNEYS</h4><div class="pip"></div>
      <p>Expert witness: Daniel Harrow is qualified as an expert witness in matters of General Average and marine insurance practice.</p>
      <a class="more">LEARN MORE</a>
    </div>
  </div>
</section>

<section class="resources">
  <h2 class="serif">RESOURCES</h2>
  <span class="rule"></span>
  <div class="res-grid">
    <div class="res"><div class="img" role="img" aria-label="Container ship with smoke at sea" style="background:linear-gradient(180deg,#8e9aa5,#3f5f7e)"></div><h5>marine surveying<br>and casualty investigation<br>world has become</h5></div>
    <div class="res hl"><div class="img" role="img" aria-label="Hand signing a document" style="background:linear-gradient(135deg,#2c3a3a,#c9cfd2)"></div><h5>marine surveying<br>and casualty investigation<br>world has become</h5></div>
    <div class="res"><div class="img" role="img" aria-label="Business handshake across a desk" style="background:linear-gradient(135deg,#3a4250,#a88a6a)"></div><h5>marine surveying<br>and casualty investigation<br>world has become</h5></div>
  </div>
  <a class="btn view">View More</a>
</section>

<footer class="footer">
  <a class="brand"><span class="dot"></span>KELVORIN</a>
  <p class="about-f">Here we briefly summarize the types of claim we principally handle. If you don’t see what you are looking for, tell us and we can discuss whether we can conscientiously take it on. Successful claim outcomes revolve<a>Read more</a></p>
  <h6 style="left:597px">QUICK LINKS</h6>
  <ul class="links"><li>Home</li><li>Claims Handled</li><li>General Average</li><li>Staff</li><li>Resources</li><li>Contact Us</li></ul>
  <h6 style="left:794px">CONTACT US</h6>
  <div class="cinfo">
    <div><span class="ic">&#9679;</span><span>1180 Harbor Road 14,<br>Cold Spring Bay, NY 11724, USA</span></div>
    <div><span class="ic">&#9990;</span><span>+1 (555) 014-2290</span></div>
    <div><span class="ic">&#9993;</span><span>info@kelvorin.com</span></div>
  </div>
  <div class="totop"><svg width="14" height="14" viewBox="0 0 14 14" fill="none" stroke="#fff" stroke-width="2"><path d="M3 7 L7 3 L11 7 M3 12 L7 8 L11 12"/></svg></div>
  <div class="divider"></div>
  <p class="copy">© 2024 THE KELVORIN COMPANY – KELVORIN &nbsp;|&nbsp; All Rights Reserved</p>
  <div class="fsoc"><i aria-label="Social profile 1"></i><i aria-label="Social profile 2"></i><i class="on" aria-label="Social profile 3"></i><i aria-label="Social profile 4"></i></div>
</footer>

</body>
</html>
```